Medical Skincare services/menu/pricing Booklet 12 pages

We need produce a 12-page glossy, saddle-stitched booklet (5 1/2" tall X 81/2" wide). The booklet will be used as a services menu for a skin care salon. I have mocked up the booklet (w/ all copy) in WORD and I've provided a separate PDF of the accurate page order (see files attached). IMPORTANT: Feel free to use your creativity yet style-wise it should kinda match my wife's website colors and text style. Her clients are demanding so she wants a clean, high end, modern look (ala Pebble maybe?). See her website for a frame of reference www.GlowWithMarta.com

Target Market(s)

upscale female, professional women, teens with acne

Industry/Entity Type

Medical

Requirements
Must have
• the pics in the mock up are important. I've attached them here

```html
<!DOCTYPE html>
<html lang="en">
<head>
<meta charset="utf-8">
<title>Glow with Marta – Services Booklet Covers</title>
<link rel="stylesheet" href="https://fonts.googleapis.com/css2?family=Open+Sans:wght@300;400;600;700&display=swap">
<style>
  :root {
    --backdrop: #a3a3a3;
    --ink: #050505;
    --silver: #cfcfcf;
    --silver-dim: #8c8c8c;
    --white: #ffffff;
    --photo-light: #d9d9d9;
    --photo-mid: #a9a9a9;
    --dot: #7d7d7d;
  }
  * { box-sizing: border-box; margin: 0; padding: 0; }
  html, body { width: 1200px; height: 900px; overflow: hidden; }
  body {
    background: var(--backdrop);
    font-family: "Open Sans", Arial, sans-serif;
    position: relative;
  }
  .booklet {
    position: absolute;
    width: 520px;
    height: 336px;
    background: var(--ink);
    overflow: hidden;
  }
  .front-cover { left: 60px; top: 110px; }
  .back-cover { left: 620px; top: 454px; }

  /* Front cover */
  .brand-name {
    position: absolute;
    left: 0; right: 0; top: 112px;
    text-align: center;
    font-weight: 700;
    font-size: 46px;
    letter-spacing: 2px;
    color: var(--silver);
    line-height: 1;
  }
  .front-web {
    position: absolute;
    left: 150px; bottom: 60px;
    font-size: 17px;
    font-weight: 400;
    color: var(--silver);
  }
  .front-web strong { font-weight: 600; }
  .front-rule {
    position: absolute;
    left: 150px; bottom: 52px;
    width: 120px; height: 2px;
    background: linear-gradient(90deg, var(--silver-dim), var(--silver));
  }
  .front-band {
    position: absolute;
    left: 60px; right: 0; bottom: 30px;
    height: 1px;
    background: var(--silver-dim);
  }

  /* Back cover */
  .portrait-panel {
    position: absolute;
    left: 0; top: 36px;
    width: 236px; height: 300px;
    background: linear-gradient(180deg, var(--photo-light), var(--photo-mid));
  }
  .name-bar {
    position: absolute;
    left: 0; bottom: 14px;
    width: 262px; height: 56px;
    background: var(--ink);
    padding: 10px 0 0 40px;
    color: var(--silver);
    font-weight: 300;
    font-size: 12px;
    line-height: 1.35;
  }
  .name-bar .person { font-size: 13px; letter-spacing: 0.5px; }
  .info-column {
    position: absolute;
    right: 22px; top: 22px;
    width: 240px;
    text-align: right;
    color: var(--white);
  }
  .book-title { font-weight: 700; font-size: 17px; line-height: 1.35; letter-spacing: 0.3px; }
  .book-web { font-size: 16px; line-height: 1.35; margin-top: 1px; }
  .book-web strong { font-weight: 600; }
  .book-web svg { vertical-align: -2px; margin-right: 6px; }
  .hours { margin-top: 7px; font-size: 9px; line-height: 1.3; font-weight: 400; }
  .studio { margin-top: 10px; font-size: 10px; line-height: 1.4; }
  .studio .studio-name { font-weight: 600; }
  .contact-line svg { vertical-align: -1px; margin-right: 4px; }
  .social-row {
    position: absolute;
    right: 30px; bottom: 70px;
    display: flex; gap: 5px;
  }
  .social-row span {
    width: 13px; height: 13px; border-radius: 50%;
    background: var(--dot);
  }
  .back-rule {
    position: absolute;
    left: 262px; right: 102px; bottom: 76px;
    height: 2px;
    background: linear-gradient(90deg, var(--silver-dim), var(--silver));
  }
</style>
</head>
<body>

  <section class="booklet front-cover">
    <h1 class="brand-name">GLOW WITH MARTA</h1>
    <p class="front-web">www.<strong>GlowWithMarta</strong>.com</p>
    <div class="front-rule"></div>
    <div class="front-band"></div>
  </section>

  <section class="booklet back-cover">
    <div class="portrait-panel" role="img" aria-label="Portrait photo of the owner in a grey knit wrap and faux-fur scarf against a light grey backdrop"></div>
    <div class="name-bar">
      <p class="person">MARTA LINDEN</p>
      <p>(MEDICAL AESTHETICIAN &amp; OWNER)</p>
    </div>

    <div class="info-column">
      <p class="book-title">BOOK ONLINE</p>
      <p class="book-web">
        <svg width="11" height="13" viewBox="0 0 11 13" aria-hidden="true"><path d="M3.5 1v7l-1.5-1.5L1 7.5 4.5 12H9l1-4-4-1.2V1z" fill="none" stroke="#fff" stroke-width="1"/></svg>www.<strong>GlowWithMarta</strong>.com
      </p>
      <div class="hours">
        <p>Sunday: Closed</p>
        <p>Monday: 10:00am–4:00pm</p>
        <p>Tuesday: 10:00am–6:00pm</p>
        <p>Wednesday: 10:00am–6:00pm</p>
        <p>Thursday: 10:00am–6:00pm</p>
        <p>Friday: 10:00am–4:00pm</p>
        <p>Saturday: 10:00am–4:00pm</p>
      </div>
      <div class="studio">
        <p class="studio-name">Glow with Marta</p>
        <p class="contact-line"><svg width="8" height="11" viewBox="0 0 8 11" aria-hidden="true"><path d="M4 10.5S0.8 6.6 0.8 4a3.2 3.2 0 0 1 6.4 0C7.2 6.6 4 10.5 4 10.5z" fill="none" stroke="#fff"/><circle cx="4" cy="4" r="1.1" fill="#fff"/></svg>4120 Alder Way #310</p>
        <p>Brookfield, CO 80999</p>
        <p class="contact-line"><svg width="10" height="10" viewBox="0 0 10 10" aria-hidden="true"><circle cx="5" cy="5" r="4.3" fill="none" stroke="#fff"/><path d="M3.4 2.8l1 1-.6.7c.4.8 1 1.4 1.8 1.8l.7-.6 1 1-.7.8C4.7 7.3 2.7 5.3 2.6 3.5z" fill="#fff"/></svg>555-014-2270</p>
        <p class="contact-line"><svg width="11" height="8" viewBox="0 0 11 8" aria-hidden="true"><rect x="0.5" y="0.5" width="10" height="7" fill="none" stroke="#fff"/><path d="M0.5 0.5l5 4 5-4" fill="none" stroke="#fff"/></svg>Marta@GlowWithMarta.com</p>
      </div>
    </div>

    <div class="social-row" aria-hidden="true"><span></span><span></span><span></span><span></span></div>
    <div class="back-rule"></div>
  </section>

</body>
</html>
```